ONE PAGE WEB DESIGN NEEDED for Finance Company

We need a web design (ONE PAGE DESIGN ONLY) for a new finance website called Brightwell Lending. Brightwell Lending helps customers get the right loan, whether its a home loan, investment loan, business loan etc.

You are required to come up with just the homepage design. Professionalism and quality is the key factors in the successful design.

Here are a few design questions to help you out:

-
What information should be used on the page?
Ive provided a document which outlines all the information needed to put on homepage (attached to the brief - called brightwell_page_info). Also see the Must Have section below on this brief.

-
What links should appear in the navigation/footer?:
The navigation should provide links to the following pages (NOTE: services link has subcategories):
1 Homepage
2 Services
- Home loans
- Investment loans
- Refinancing loans
- Business loans
3 About Us
4 FAQ
5 Contact Us

-
What colors should be used in the design?
Our company colors - Cyan: #2EADE3, Blue: #004B70, White. Feel free to submit designs with slight variations if you feel it improves the design.

-
What should the layout of the page be?
This is up to you to come up with - we are open to different layouts for the page design (as long as they capture the information effectively and making it easy to understand).

Target Market(s)

Potential Home owners, Families and Business Owners

Industry/Entity Type

Business

Requirements
Must have
• - Must contain our logo (attached as PNG and Illustrator file)
- Winning designer must supply a Photoshop file (PSD) that will allow us.
Nice to have
• - Should include photos/images of families, professional groups, tradespeople etc (you can use stock photos from PixQuarry and I will purchase them once you are selected as the winning design)
- Link to a loan calculator somewhere on front page with a button 'Find out how much you could borrow' (or maybe even try adding a loan calculator to the homepage if you think this would look good)
- Page should have a main headline "Finding the right loan for you" or "Brightwell Lending finds the right loan for our customers."
- Must include Accreditation logos somewhere on the homepage (will try and supply these soon)
Should not have
• - Poor quality designs will not be considered
- Do not use clipart

```html
<!DOCTYPE html>
<html lang="en">
<head>
<meta charset="utf-8">
<title>Brightwell Lending – Finding the Right Loan for you</title>
<link href="https://fonts.googleapis.com/css2?family=Source+Sans+3:wght@300;400;600;700&family=PT+Sans+Narrow:wght@700&display=swap" rel="stylesheet">
<style>
:root{
  --cyan:#2eade3;
  --cyan-dark:#1f9bd6;
  --blue:#004b70;
  --navy:#0a4f74;
  --text:#5b5b5b;
  --text-dark:#333;
  --line:#e2e2e2;
  --footer:#2f2f2f;
  --white:#fff;
}
*{box-sizing:border-box;margin:0;padding:0}
html,body{width:976px;height:1200px;overflow:hidden;background:var(--white)}
body{position:relative;font-family:"Source Sans 3",Arial,sans-serif;color:var(--text);font-size:11px}
.abs{position:absolute}
.top-strip{left:0;top:0;width:976px;height:5px;background:#dcdcdc}

/* header */
.brand{left:64px;top:40px;display:flex;align-items:center;gap:9px}
.brand-mark{width:30px;height:30px;border-radius:50%;background:var(--cyan)}
.brand-name{font-size:25px;font-weight:600;color:var(--blue);letter-spacing:-.3px}
.callcenter{left:670px;top:28px;display:flex;align-items:center;gap:6px;color:var(--cyan);font-size:11px}
.callcenter strong{font-weight:400;color:var(--blue);font-size:16px;margin-left:3px}
.main-nav{left:0;top:79px;height:30px;width:976px}
.main-nav a{position:absolute;top:0;height:30px;line-height:30px;color:var(--blue);text-decoration:none;font-size:14px}
.main-nav a.active{background:var(--navy);color:var(--white);padding:0 16px;border-radius:2px 2px 0 0}
.dropdown{left:550px;top:109px;width:130px;height:116px;background:var(--cyan);z-index:5;padding:6px 12px}
.dropdown li{list-style:none;height:24px;line-height:24px;border-bottom:1px solid rgba(255,255,255,.3);color:var(--white);font-size:11.5px;padding-left:7px;position:relative}
.dropdown li:last-child{border-bottom:0}
.dropdown li::before{content:"";position:absolute;left:0;top:9px;border-left:3px solid #fff;border-top:3px solid transparent;border-bottom:3px solid transparent}

/* hero */
.hero-band{left:0;top:120px;width:976px;height:353px;background:linear-gradient(#4cbcea,var(--cyan))}
.hero-rule{left:0;top:473px;width:976px;height:6px;background:var(--blue)}
.hero-photo{left:48px;top:135px;width:878px;height:328px;border:3px solid var(--white);border-radius:12px;overflow:hidden;
  background:linear-gradient(100deg,#c9d6e2 0%,#9fb6cc 25%,#e8eef2 45%,#f4f6f7 70%,#dfe4e6 100%)}
.hero-caption{left:0;top:180px;width:100%;height:78px;background:linear-gradient(90deg,rgba(255,255,255,0) 40%,rgba(255,255,255,.6) 60%)}
.hero-title{left:436px;top:192px;font-size:34px;font-weight:300;color:var(--blue);white-space:nowrap}
.slider-tab{left:452px;top:442px;width:62px;height:21px;background:var(--navy);border-radius:10px 10px 0 0;display:flex;justify-content:center;align-items:center;gap:4px;z-index:3}
.slider-tab span{width:6px;height:6px;border-radius:50%;background:var(--white)}

/* services */
.services{left:0;top:479px;width:976px;height:176px;background:linear-gradient(#fff,#f2f2f2)}
.service{position:absolute;top:0;height:176px;padding-top:16px}
.service + .service{border-left:1px solid var(--line)}
.service h2{font-family:"PT Sans Narrow",Arial,sans-serif;font-size:19px;color:var(--blue);display:flex;align-items:center;gap:6px;height:30px}
.service p{margin-top:6px;line-height:17px;color:var(--text)}
.service ul{margin-top:8px;list-style:none}
.service li{line-height:21.5px;padding-left:15px;position:relative;color:#444}
.service li::before{content:"";position:absolute;left:5px;top:8px;border-left:3px solid #555;border-top:3px solid transparent;border-bottom:3px solid transparent}

/* welcome */
.welcome-title{left:65px;top:688px;font-size:19px;font-weight:400;color:var(--text-dark)}
.welcome-title b{font-weight:600}
.welcome-photo{left:65px;top:724px;width:170px;height:137px;background:linear-gradient(135deg,#dfe9f1,#7fa9c9 55%,#2e6f9e)}
.lead{left:249px;top:723px;width:428px;font-weight:700;color:var(--text-dark);line-height:17px}
.body-copy{line-height:17.2px;text-align:justify;color:#6a6a6a}
.copy-1{left:249px;top:761px;width:428px}
.copy-2{left:62px;top:872px;width:615px}
.copy-3{left:62px;top:928px;width:615px}

/* sidebar */
.calc-title{left:721px;top:688px;font-size:19.5px;line-height:23px;color:var(--blue);font-weight:400}
.calc-title b{font-weight:600}
.calc-photo{left:718px;top:740px;width:189px;height:111px;border:1px solid #ccc;border-radius:6px;background:linear-gradient(160deg,#f3f4f5,#cfd6dc 50%,#8a99a8)}
.calc-note{left:721px;top:856px;width:190px;line-height:17px;color:#888}
.calc-btn{left:722px;top:896px;width:107px;height:26px;background:var(--navy);color:var(--white);font-size:10.5px;line-height:26px;text-align:center;border-radius:2px;letter-spacing:.2px}

/* accreditation */
.divider{left:50px;top:1024px;width:875px;height:1px;background:var(--line)}
.accreditations{left:92px;top:1043px;width:770px;height:44px;display:flex;justify-content:space-between;align-items:center}
.badge{background:#d8d8d8;border-radius:4px;height:30px}
.badge.round{border-radius:50%;width:44px;height:44px}

/* footer */
.footer{left:0;top:1119px;width:976px;height:81px;background:var(--footer);border-top:4px solid #444}
.copyright{left:64px;top:1145px;color:#ddd;font-size:10.5px}
.footer-nav{left:526px;top:1144px;display:flex;font-size:11px;color:var(--white)}
.footer-nav span{padding:0 8px;border-left:1px solid #bbb}
.footer-nav span:first-child{border-left:0;padding-left:0;padding-right:14px}
.social{left:825px;top:1140px;display:flex;gap:5px}
.social span{width:23px;height:23px;border-radius:50%;background:#f2f2f2}
</style>
</head>
<body>
<div class="abs top-strip"></div>

<header>
  <div class="abs brand"><span class="brand-mark"></span><span class="brand-name">Brightwell Lending</span></div>
  <div class="abs callcenter">
    <svg width="16" height="16" viewBox="0 0 16 16" aria-hidden="true"><path d="M3 2c2 0 3 3 2 4l-1 1c1 2 3 4 5 5l1-1c1-1 4 0 4 2 0 1-1 2-2 2C7 15 1 9 1 4c0-1 1-2 2-2z" fill="var(--cyan)"/></svg>
    Call Center Solutions: <strong>+1800.555.0142</strong>
  </div>
  <nav class="abs main-nav">
    <a style="left:497px">Home</a>
    <a class="active" style="left:550px">Services</a>
    <a style="left:659px">About Us</a>
    <a style="left:757px">FAQ</a>
    <a style="left:823px">Contact Us</a>
  </nav>
  <ul class="abs dropdown">
    <li>Home loans</li><li>Investment loans</li><li>Refinancing loans</li><li>Business loans</li>
  </ul>
</header>

<section>
  <div class="abs hero-band"></div>
  <div class="abs hero-photo" role="img" aria-label="Smiling woman in a bright office beside a desk lamp and computer monitors">
    <div class="abs hero-caption"></div>
    <h1 class="abs hero-title">Finding the Right Loan for you</h1>
  </div>
  <div class="abs slider-tab"><span></span><span></span><span></span><span></span></div>
  <div class="abs hero-rule"></div>
</section>

<section class="abs services">
  <div class="service" style="left:0;width:262px;padding-left:68px">
    <h2><svg width="28" height="24" viewBox="0 0 28 24" aria-hidden="true"><path d="M14 1 1 12h4v11h7v-7h4v7h7V12h4z" fill="var(--cyan)"/></svg>Home loans</h2>
    <p>Pellentesque habitant morbi tristique senectus et netus et malesuada:-</p>
    <ul><li>Home buyers</li><li>First home buyers</li><li>Over 20 lenders</li></ul>
  </div>
  <div class="service" style="left:262px;width:213px;padding-left:22px">
    <h2><svg width="26" height="26" viewBox="0 0 26 26" aria-hidden="true"><circle cx="13" cy="13" r="11.5" fill="none" stroke="var(--cyan)" stroke-width="2.5"/><circle cx="13" cy="13" r="8" fill="var(--cyan)"/><text x="13" y="18" text-anchor="middle" font-size="13" font-weight="700" fill="#fff" font-family="Arial,sans-serif">$</text></svg>Investment loans</h2>
    <p>Pellentesque habitant morbi tristique senectus et netus et malesuada:-</p>
    <ul><li>Property investment loans</li><li>Interest only loans</li></ul>
  </div>
  <div class="service" style="left:475px;width:231px;padding-left:22px">
    <h2><svg width="26" height="26" viewBox="0 0 26 26" aria-hidden="true"><rect x="2" y="10" width="5" height="14" fill="var(--cyan)"/><rect x="10" y="2" width="5" height="22" fill="var(--cyan)"/><rect x="18" y="7" width="5" height="17" fill="var(--cyan)"/><rect x="0" y="24" width="26" height="2" fill="var(--cyan)"/></svg>Refinancing loans</h2>
    <p>Pellentesque habitant morbi tristique senectus et netus et malesuada:-</p>
    <ul><li>Refinancing for the best rate</li><li>Upsizing or downsizing</li><li>Change from a variable to a fixed rate</li></ul>
  </div>
  <div class="service" style="left:706px;width:270px;padding-left:24px">
    <h2><svg width="28" height="24" viewBox="0 0 28 24" aria-hidden="true"><path d="M10 5V2h8v3" fill="none" stroke="var(--cyan)" stroke-width="2.5"/><rect x="1" y="5" width="26" height="18" fill="var(--cyan)"/></svg>Business loans</h2>
    <p>Pellentesque habitant morbi tristique senectus et netus et malesuada:-</p>
    <ul><li>Long term</li><li>Short term</li><li>Equipment and Leasing</li></ul>
  </div>
</section>

<main>
  <h2 class="abs welcome-title">Welcome to <b>Brightwell Lending</b> Mainpage..</h2>
  <div class="abs welcome-photo" role="img" aria-label="Professional reviewing charts on a laptop and tablet"></div>
  <p class="abs lead">Pellentesque habitant morbi tristique senectus et netus et malesuada fames ac turpis egestas. In posuere felis nec tortor. Pellentesque faucibus.</p>
  <p class="abs body-copy copy-1">Ut accumsan ultricies elit. Maecenas at justo id velit placerat molestie. Donec dictum lectus non odio. Cras a ante vitae enim iaculis aliquam. Mauris nunc quam, venenatis nec, euismod sit amet, egestas placerat, est. Pellentesque habitant morbi tristique senectus et netus et malesuada fames ac turpis egestas. Cras id elit. Integer quis urna. Ut ante enim, dapibus malesuada, fringilla eu, condimentum quis, tellus. Aenean porttitor eros vel dolor. Donec convallis pede venenatis nibh. Duis quam. Nam eget lacus. Aliquam erat volutpat.</p>
  <p class="abs body-copy copy-2">Mauris vel lacus vitae felis vestibulum volutpat. Etiam est nunc, venenatis in, tristique eu, imperdiet ac, nisl. Cum sociis natoque penatibus et magnis dis parturient montes, nascetur ridiculus mus. In iaculis facilisis massa. Etiam eu urna. Sed porta. Suspendisse quam leo, molestie sed, luctus quis, feugiat in, pede.</p>
  <p class="abs body-copy copy-3">Nunc tempus felis vitae urna. Vivamus porttitor, neque at volutpat rutrum, purus nisi eleifend libero, a tempus libero lectus feugiat felis. Morbi diam mauris, viverra in, gravida eu, mattis in, ante. Morbi eget arcu. Morbi porta, libero id ullamcorper nonummy, nibh ligula pulvinar metus, eget consectetuer augue nisi quis lacus. Ut ac mi quis lacus mollis aliquam.</p>
</main>

<aside>
  <h2 class="abs calc-title">Find how much<br><b>you could borrow</b></h2>
  <div class="abs calc-photo" role="img" aria-label="Hand pressing keys on a calculator"></div>
  <p class="abs calc-note">Mauris vel lacus vitae felis vestibulum volutpat. Etiam est nunc.</p>
  <div class="abs calc-btn">CALCULATE NOW</div>
</aside>

<div class="abs divider"></div>
<div class="abs accreditations" aria-label="Accreditations">
  <span class="badge" style="width:76px"></span>
  <span class="badge" style="width:42px;height:36px"></span>
  <span class="badge" style="width:96px"></span>
  <span class="badge" style="width:40px"></span>
  <span class="badge" style="width:80px"></span>
  <span class="badge round"></span>
  <span class="badge" style="width:82px;height:24px"></span>
  <span class="badge" style="width:82px"></span>
</div>

<footer>
  <div class="abs footer"></div>
  <p class="abs copyright">Copyright © 2012 Company Name.&nbsp; All right reserved</p>
  <nav class="abs footer-nav"><span>Home</span><span>Services</span><span>About Us</span><span>FAQ</span><span>Contact Us</span></nav>
  <div class="abs social"><span></span><span></span><span></span><span></span></div>
</footer>
</body>
</html>
```